Business Card Design Project

Personal Service. There are three areas of my service: Resourceful/Recycling Consultation, Life Coaching using Law of Attraction & Visualization Board. My current cards has: Visualization to Manifestation. I would like to work with this theme

Industry/Entity Type

Business

Contact Information for Business Card

Circles. Recyling Triangle

```html
<!DOCTYPE html>
<html lang="en">
<head>
<meta charset="utf-8">
<title>Dana Whitfield – Business Card</title>
<link href="https://fonts.googleapis.com/css2?family=Roboto:wght@400;500;700&display=swap" rel="stylesheet">
<style>
  :root {
    --page: #e9eaec;
    --card: #ffffff;
    --brand-blue: #0a7fb5;
    --brand-green: #2fcf3a;
    --sun-yellow: #f2e81a;
    --ink: #1d2b3a;
    --rule: #2b4a5c;
    --faint: #ececec;
  }
  * { margin: 0; padding: 0; box-sizing: border-box; }
  html, body { width: 1200px; height: 900px; overflow: hidden; }
  body {
    background: var(--page);
    font-family: "Roboto", Arial, sans-serif;
    position: relative;
  }
  .business-card {
    position: absolute;
    left: 75px; top: 150px;
    width: 1050px; height: 600px;
    background: var(--card);
    border-radius: 36px;
    overflow: hidden;
    box-shadow: 0 10px 30px rgba(0,0,0,.15);
  }
  .card-art { position: absolute; inset: 0; }
  .brand {
    position: absolute;
    left: 90px; top: 70px;
    display: flex; align-items: center; gap: 22px;
  }
  .brand-dot {
    width: 70px; height: 70px; border-radius: 50%;
    background: var(--brand-blue);
  }
  .brand-name {
    font-size: 58px; font-weight: 500;
    color: var(--brand-blue);
    letter-spacing: 1px;
    text-transform: uppercase;
  }
  .title {
    position: absolute;
    left: 182px; top: 150px;
    font-size: 25px; font-weight: 500;
    color: var(--brand-green);
    line-height: 1.15;
    text-transform: uppercase;
  }
  .divider {
    position: absolute;
    left: 90px; top: 230px;
    width: 760px; height: 2px;
    background: var(--rule);
  }
  .contacts {
    position: absolute;
    left: 90px; top: 255px;
    list-style: none;
  }
  .contacts li {
    display: flex; align-items: center; gap: 14px;
    font-size: 24px; color: var(--ink);
    margin-bottom: 10px;
  }
  .contact-icon {
    width: 28px; height: 28px; border-radius: 50%;
    background: var(--brand-green);
    display: flex; align-items: center; justify-content: center;
  }
</style>
</head>
<body>
  <main class="business-card">
    <svg class="card-art" viewBox="0 0 1050 600" width="1050" height="600" aria-hidden="true">
      <circle class="faint-mark" cx="880" cy="250" r="170" fill="var(--faint)"/>
      <path class="green-swoosh" d="M0 300 C 300 400, 650 450, 1050 455 L1050 600 L0 600 Z" fill="var(--brand-green)"/>
      <path class="white-gap" d="M0 312 C 300 420, 650 478, 1050 484 L1050 600 L0 600 Z" fill="var(--card)"/>
      <path class="blue-band" d="M0 318 C 300 428, 650 488, 1050 494 L1050 600 L0 600 Z" fill="var(--brand-blue)"/>
    </svg>

    <div class="brand">
      <span class="brand-dot"></span>
      <span class="brand-name">Dana Whitfield</span>
    </div>
    <p class="title">Interfaith Minister and<br>Certified Life Coach</p>

    <div class="divider"></div>

    <ul class="contacts">
      <li>
        <span class="contact-icon">
          <svg width="16" height="16" viewBox="0 0 24 24"><path fill="#fff" d="M6.6 10.8a15 15 0 0 0 6.6 6.6l2.2-2.2c.3-.3.7-.4 1-.2 1.1.4 2.3.6 3.6.6.6 0 1 .4 1 1V20c0 .6-.4 1-1 1A17 17 0 0 1 3 4c0-.6.4-1 1-1h3.5c.6 0 1 .4 1 1 0 1.3.2 2.5.6 3.6.1.3 0 .7-.2 1z"/></svg>
        </span>
        555-014-2290 (Appointment only)
      </li>
      <li>
        <span class="contact-icon">
          <svg width="16" height="16" viewBox="0 0 24 24"><path fill="#fff" d="M3 6h18v12H3z"/><path fill="none" stroke="#2fcf3a" stroke-width="2" d="M3 6l9 7 9-7"/></svg>
        </span>
        Dana@revdanawhitfield.com
      </li>
    </ul>
  </main>
</body>
</html>
```